EmberDepot, Charcoal bag packaging and brand

I'm looking at a package design for 10 KG/22 pounds of charcoal.
The design must include a name that is catchy and conveys quality, heat and low ash. The name must not violate any trademarks or tradenames. One of the best resources to view other packaging is the Quiet Pelican website. www.quietpelican.com
Two colors only and one must be red which will be printed on a kraft paper bag. The name EMBERDEPOT.COM must be prominent and also list our website of www.emberdepot.com.
Updates
Here is some wording for the front of the bag and it can be in any order. Make it look GREAT! Use the name "Blazewood Charcoal", but the Emberdepot logo should be the most prominant. Hi Heat, Low Ash, Long burning We will need some wording on the back and sides, but it's primarily just text and we won't worry about it until later. A UPC code will be necessary also. Thanks, Rick Tolben
100% Natural Hardwood Lump Charcoal
Restaurant and Competition grade
No additives, No fillers
Non sparking
Easy lighting, use a chimney starter
Mild flavor profile
A number of the designs are using full coverage ink.
Please limit the amount of ink coverage to no more than 25% ..
It becomes very costly to use 100% coverage.
Thanks!
Rick Tolben
Thank you to all the fine designers.
It was an extremely difficult decision for us. One fine designer was knocked out of the competition by our attorneys and we also received notice from the same attorneys that our brand of "Blazewood Charcoal" won't work...
I'll be posting another new logo design for branding of the charcoal at some point.
Kindest regards to all.
Rick Tolben
Target Market(s)
End users, restaurants, resorts, competition cookoffs
Look and feel
Each slider illustrates characteristics of the customer's brand and the style your logo design should communicate.

```html
<!DOCTYPE html>
<html lang="en">
<head>
<meta charset="utf-8">
<title>Ember Depot – Blazewood Charcoal Bag Front</title>
<link href="https://fonts.googleapis.com/css2?family=Arimo:wght@700&family=Archivo+Black&display=swap" rel="stylesheet">
<style>
  :root {
    --backdrop: #dcdcdc;
    --kraft: #dcc09c;
    --kraft-light: #e6cfae;
    --kraft-dark: #cfae86;
    --red: #c41a1f;
    --white: #ffffff;
    --char: #555555;
    --char-dark: #3f3f3f;
    --shadow: #4a4a4a;
  }
  * { margin: 0; padding: 0; box-sizing: border-box; }
  html, body { width: 1200px; height: 900px; overflow: hidden; background: var(--backdrop); }
  .bag-front {
    position: absolute; left: 292px; top: 0; width: 640px; height: 900px;
    background:
      radial-gradient(ellipse at 30% 20%, var(--kraft-light), transparent 60%),
      radial-gradient(ellipse at 75% 70%, var(--kraft-light), transparent 55%),
      radial-gradient(ellipse at 80% 15%, var(--kraft-dark), transparent 50%),
      var(--kraft);
    font-family: "Arimo", Arial, sans-serif;
  }
  .tagline-band {
    position: absolute; left: 0; top: 24px; width: 640px; height: 70px;
    background: var(--white); color: var(--red);
    font-size: 26px; font-weight: 700; text-align: center; line-height: 70px;
  }
  .flame-art {
    position: absolute; left: 176px; top: 112px; width: 276px; height: 414px;
    border-radius: 45% 45% 40% 40% / 60% 60% 35% 35%;
    background: radial-gradient(ellipse at 50% 65%, #666, #4d4d4d 70%, rgba(77,77,77,0.85));
  }
  .brand-name {
    position: absolute; left: 0; width: 640px; top: 208px; text-align: center;
    font-family: "Archivo Black", "Arial Black", sans-serif;
    font-size: 66px; line-height: 80px; color: var(--white);
    text-shadow: 4px 5px 0 var(--shadow);
  }
  .product-name {
    position: absolute; left: 0; width: 640px; top: 300px; text-align: center;
    font-family: "Archivo Black", "Arial Black", sans-serif;
    font-size: 78px; line-height: 106px; color: var(--red);
    text-shadow: -3px -3px 0 var(--white);
  }
  .benefits { position: absolute; left: 160px; top: 542px; list-style: none; }
  .benefits li {
    display: flex; align-items: center; height: 40px;
    color: var(--red); font-size: 34px; font-weight: 700;
  }
  .benefits svg { width: 54px; height: 44px; margin-right: 18px; }
  .features {
    position: absolute; left: 20px; top: 702px; width: 588px; height: 156px;
    border: 5px solid var(--white); border-radius: 10px;
    background: radial-gradient(ellipse at 60% 40%, #606060, var(--char-dark));
    padding: 16px 10px; list-style: none;
  }
  .features li { color: var(--red); font-size: 19px; font-weight: 700; line-height: 25px; }
</style>
</head>
<body>
  <main class="bag-front">
    <header class="tagline-band">100% Natural&nbsp; Hardwood Lump Charcoal</header>
    <div class="flame-art" role="img" aria-label="Large dark grey flame illustration with red accent lines"></div>
    <h1 class="brand-name">Ember Depot</h1>
    <h2 class="product-name">Blazewood<br>Charcoal</h2>
    <ul class="benefits">
      <li><svg viewBox="0 0 54 44" aria-hidden="true"><path d="M2 24 L12 18 L22 30 L46 2 L52 6 L22 42 Z" fill="#555"/></svg>High Heat</li>
      <li><svg viewBox="0 0 54 44" aria-hidden="true"><path d="M2 24 L12 18 L22 30 L46 2 L52 6 L22 42 Z" fill="#555"/></svg>Low Ash</li>
      <li><svg viewBox="0 0 54 44" aria-hidden="true"><path d="M2 24 L12 18 L22 30 L46 2 L52 6 L22 42 Z" fill="#555"/></svg>Long Burning</li>
    </ul>
    <ul class="features">
      <li>Restaurant and Competition grade</li>
      <li>No additives, No fillers</li>
      <li>Non sparking</li>
      <li>Easy lighting, use a chimney starter</li>
      <li>Mild flavor profile</li>
    </ul>
  </main>
</body>
</html>
```